Vantor Grid Advisory Partners - Website

Design & Build a website for a new company which operates in the Systems and Technology space for Transportation, Government and Commercial sectors.

Overall design should be minimalist in nature.
Should also have a feed that provides news and event updates on the main page.
Logo has already been awarded and should be incorporated into the site.

We like the overall layout, functionality and simplicity of the below sites. Submitted designs could be similar to or a combination of the aspects on these sites, or perhaps a whole different concept - we are open to new ideas.
Morqeli.com
Tumb.it

All I am moving away from the Tumb.it website and would like it to be more aligned with Morqeli.com not only in layout but in functionality. I will be extending the deadline of this design brief for two weeks to incorporate additional requirements and will add addtional funding to the project.

Apologies for not having more information available to provide but with so many submissions its getting confusing.

Thanks Dorian

Important: We will need two language versions of the website, English and Arabic; the website is hosted on HostPivo

Hello All, Thank you for your submissions. We have narrowed it down to the final 6 designers and I just wanted to take a moment and provide a bit of feedback regarding the concepts that we like and the modifications we are looking for. First, let me mention some of the design functions we like. - At the top of the homepage we really like the "region" or "language" tab so that the website can be viewed in both English and Arabic. - We like the homepage to have clear color variation so that the different sections of the homepage are distinct. Additionally, we like the bottom portion of the homepage to be in red. We feel that draws attention to our contact information. Again, we would like the colors to integrate black, gray-scale, red, etc. - Having a search tab at the top of the home page, or integrated into the main image, so that the site is easy to navigate. - We especially like the main image to have the scrolling tabs at the bottom so it is easy to browse the services offered (Consultancy, Solutions Architecture, Masters Systems Integration, Independent Design Review). - In regards to the services offered tab we really like the idea that a few people presented that have the outside of our logo with an icon in the middle of consultancy, solutions, etc., etc. Secondly, as mentioned in our brief we really enjoy the design of morqeli site. Specially, we enjoy the strong iconic images they use, the way the tabs at the top scroll easily, and contact us page that generates an email. Lastly, I've included some photos of the concept we have been working on. What we are trying to demonstrate is how our company offers a range of services that are essentially linked together. We provide individual services that when combined present the full service package. We would like this concept to be integrated into the over concept of our website. Please feel free to ask for clarification of any of the above points or contact us if you have any additional questions. We appreciate all of your hard work and are very excited to see the updated designs. Best, Miriam Okaford Vangridex Senior Program Manager miriam.okaford@vangridax.example

Industry/Entity Type

Government

Font styles to use
Serif
Sans Serif

Requirements
Must have
• Must work on/adapt to various/mobile devices (responsive)
Must be simple and straightforward
Colors should be in line/matching with logo
2 language versions: English and Arabic (no Thai)
Services should be the first group/row of items after/below the main image
Note: the website will be hosted by hostpivo
Nice to have
• Submit feedback form
What's New section
The banner at the bottom of the site should not be too large; we would like a narrow one more
It would be nice if the header/top banner (with Home, About, etc. tabs) could stay in place as you scroll down (like Morqeli and Chatterly)
We will likely only use one image with a Company slogan on the Home page rather than a carousel of images to rotate through
Should not have
• This is the existing website: http://www.vangridex.example
We do not like the animation, the way the banner icons/titles bounce
Not simple enough, we don't like the functionality or how pages load so slowly
We do not like the logo centered - it should be at the left
The banner and its tabs should not be towards the right, we would like them to be centered, to go all the way across and to be below the logo

```html
<!DOCTYPE html>
<html lang="en">
<head>
<meta charset="utf-8">
<title>Vangridex</title>
<link rel="stylesheet" href="https://fonts.googleapis.com/css2?family=Open+Sans:wght@300;400;600;700&display=swap">
<style>
:root{
  --red:#d7141a;
  --ink:#222;
  --dark:#282828;
  --darker:#1d1d1d;
  --grey:#8a8a8a;
  --line:#d6d6d6;
  --panel:#f2f1f1;
  --strip:#d8d8d8;
}
*{margin:0;padding:0;box-sizing:border-box}
html,body{width:688px;height:1200px;overflow:hidden;background:#fff}
body{position:relative;font-family:"Open Sans",Arial,sans-serif;color:var(--ink)}
.abs{position:absolute}

.brand{left:63px;top:10px;width:90px;height:70px;display:flex;flex-direction:column;align-items:center;justify-content:center;gap:8px}
.brand-mark{width:30px;height:30px;border:4px solid var(--red)}
.brand-name{font-size:12px;font-weight:700;letter-spacing:3px;color:var(--red)}

.phone{left:511px;top:32px;font-size:11px;color:#444;display:flex;align-items:center;gap:3px}
.phone b{font-weight:600;color:#222}
.social{left:512px;top:49px;display:flex;gap:2px}
.social span{width:17px;height:17px;background:#c9c9c9}

.nav{left:63px;top:91px;width:561px;height:23px;display:flex;border:1px solid var(--line);border-left:none;font-size:8.5px}
.nav a{display:flex;align-items:center;justify-content:center;border-left:1px solid var(--line);color:#222;text-decoration:none}
.nav a.active{background:var(--ink);color:#fff;font-weight:700;border-left:none}
.nav .search{flex:1;border-left:1px solid var(--line);display:flex;align-items:center;padding-left:6px;color:#aaa;font-size:7.5px}
.nav .go{width:19px;background:var(--red);display:flex;align-items:center;justify-content:center}
.rule-top{left:0;top:113px;width:688px;height:2px;background:#ececec}

.hero{left:0;top:115px;width:688px;height:260px;background:linear-gradient(100deg,#d9d6d1 0%,#c9c6c0 45%,#dcdcdc 62%,#9fa4aa 100%)}
.hero-box{left:61px;top:179px;width:261px;height:127px;background:rgba(20,20,20,.9);padding:10px 7px;color:#fff;font-size:13.2px;line-height:16.8px;font-weight:400}
.hero-box em{font-style:normal;color:var(--red);font-weight:600}
.learn{left:64px;top:270px;width:145px;height:22px;border-radius:11px;background:#fff;display:flex;align-items:center;padding-left:10px;font-size:9.5px;color:#222}
.learn b{margin-left:3px}
.learn i{position:absolute;right:4px;top:3px;width:16px;height:16px;border-radius:50%;background:var(--red)}

.welcome{left:0;top:413px;width:688px;text-align:center;font-size:19px;font-weight:300}
.welcome b{color:var(--red);font-weight:600}
.intro{left:108px;top:448px;width:472px;text-align:center;font-size:7.6px;line-height:14px;color:#555}
.more{left:311px;top:502px;width:66px;height:19px;background:var(--ink);color:#fff;font-size:7.8px;font-weight:600;display:flex;align-items:center;justify-content:center}
.divider{left:70px;width:548px;height:8px;background:linear-gradient(#f6f6f6,#fff)}

.service{top:564px;width:126px;height:144px;border:1px solid var(--line);text-align:center;padding-top:18px}
.service h3{font-size:10.5px;font-weight:400;margin-top:6px;color:#333}
.service p{font-size:7px;line-height:10.4px;color:#999;padding:7px 12px 0}
.service.on{background:var(--dark);border-color:var(--dark);border-bottom:3px solid var(--red)}
.service.on h3{color:#fff;font-weight:700}
.service.on p{color:#fff}
.service svg{height:36px}

.head{font-size:12px;color:#333}
.acc-open{left:76px;top:781px;width:265px;height:128px;background:var(--panel)}
.acc-open .tab{position:absolute;left:0;top:0;width:23px;height:33px;background:var(--red)}
.acc-open .tab:after{content:"";position:absolute;left:7px;top:16px;width:9px;height:1px;background:#fff}
.acc-open .bar{position:absolute;left:0;top:33px;width:23px;height:95px;background:var(--strip)}
.acc-open h4{position:absolute;left:32px;top:16px;width:220px;font-size:9px;font-weight:400;line-height:11px;color:#222}
.acc-open p{position:absolute;left:32px;top:42px;width:226px;font-size:7px;line-height:11.5px;color:#999}
.acc{left:76px;width:265px;background:var(--panel);display:flex;align-items:center;font-size:8px;color:#222}
.acc i{width:23px;height:100%;background:#333;position:relative;margin-right:9px;flex:none}
.acc i:before,.acc i:after{content:"";position:absolute;left:7px;top:50%;width:9px;height:1px;background:#fff}
.acc i:after{transform:rotate(90deg)}

.news{left:377px;width:250px}
.date{position:absolute;left:0;top:0;width:36px;height:33px;text-align:center;color:#fff}
.date .d{height:18px;background:#3a3a3a;font-size:13px;line-height:18px}
.date .m{height:15px;background:var(--red);font-size:11px;line-height:15px}
.news h5{position:absolute;left:42px;top:0;font-size:9px;font-weight:400;color:#222}
.news p{position:absolute;left:42px;top:14px;width:195px;font-size:7px;line-height:11.5px;color:#999}

.foot{left:0;top:1025px;width:688px;height:150px;background:var(--dark);border-top:2px solid var(--red);color:#bbb}
.foot .logo{position:absolute;left:72px;top:16px;width:66px;display:flex;flex-direction:column;align-items:center;gap:8px}
.foot .logo span{width:24px;height:24px;border:3px solid #fff}
.foot .logo b{font-size:9.5px;letter-spacing:2.4px;color:#fff}
.foot .about{position:absolute;left:66px;top:89px;width:125px;font-size:7px;line-height:11.5px;color:#888}
.foot .sep{position:absolute;top:16px;width:1px;height:118px;background:#3a3a3a}
.foot h6{position:absolute;font-size:10.5px;font-weight:400;color:#eee}
.foot ul{position:absolute;list-style:none;font-size:7px;line-height:9px;color:#ddd}
.foot .contact{position:absolute;left:346px;top:45px;font-size:7px;line-height:10.5px;color:#999}
.map{position:absolute;left:477px;top:42px;width:148px;height:95px;background:linear-gradient(135deg,#ece9df,#dcd8c6 60%,#e9e5d8)}
.copy{left:0;top:1174px;width:688px;height:26px;background:var(--darker);color:#ccc;font-size:7px;display:flex;align-items:center;justify-content:center}
</style>
</head>
<body>

<header>
  <div class="abs brand"><span class="brand-mark"></span><span class="brand-name">VANGRIDEX</span></div>
  <div class="abs phone">
    <svg width="9" height="11" viewBox="0 0 10 12"><path d="M2 0h2l1 3-1.5 1.2c.6 1.6 1.5 2.8 2.8 3.6L7.5 6.5 10 8v2.4L8.6 12C4 11 1 7 0 2z" fill="#d7141a"/></svg>
    Call Us : <b>+100 555 0142</b>
  </div>
  <div class="abs social" aria-label="Social links"><span></span><span></span><span></span><span></span><span></span><span></span></div>
  <nav class="abs nav">
    <a class="active" style="width:60px" href="#">HOME</a>
    <a style="width:94px" href="#">Business Units</a>
    <a style="width:72px" href="#">Services</a>
    <a style="width:74px" href="#">About Us</a>
    <a style="width:70px" href="#">Locations</a>
    <a style="width:74px" href="#">Contact Us</a>
    <div class="search">Search</div>
    <div class="go"><svg width="9" height="9" viewBox="0 0 10 10"><circle cx="4" cy="4" r="3" fill="none" stroke="#fff" stroke-width="1.4"/><path d="M6.2 6.2 9 9" stroke="#fff" stroke-width="1.6"/></svg></div>
  </nav>
  <div class="abs rule-top"></div>
</header>

<section>
  <div class="abs hero" role="img" aria-label="Overhead photo of business team meeting around a glass table in a bright office"></div>
  <div class="abs hero-box"><em>VANGRIDEX</em> Specializes in delivering Quality Professional Services and Technical Projects that Support larger Business goals.</div>
  <a class="abs learn">LEARN MORE <b>ABOUT US</b><i><svg width="16" height="16" viewBox="0 0 16 16"><path d="M4 8h7M8 5l3 3-3 3" stroke="#fff" stroke-width="1.8" fill="none"/></svg></i></a>
</section>

<section>
  <h1 class="abs welcome">Welcome to <b>VANGRIDEX</b></h1>
  <p class="abs intro">We  specializes in delivering quality professional services and technical projects that support larger business goals.  systems are tools that support a greater business function and need. we understand that most technical projects are conceptualized to support a larger vision with actual business goals in mind and ensure that all of our professional</p>
  <a class="abs more">Read More</a>
  <div class="abs divider" style="top:545px"></div>
</section>

<section>
  <div class="abs service" style="left:67px">
    <svg viewBox="0 0 40 36" width="40"><circle cx="15" cy="10" r="6" fill="#222"/><circle cx="26" cy="10" r="6" fill="#222"/><path d="M4 30c0-8 5-12 11-12s11 4 11 12z" fill="#222"/><path d="M17 30c0-8 4-12 9-12s10 4 10 12z" fill="#222"/></svg>
    <h3>Consulting</h3>
    <p>Lorem Ipsum is simply dummy text of the printing and typesetting industry. Lorem Ipsum has been the industry's</p>
  </div>
  <div class="abs service on" style="left:210px">
    <svg viewBox="0 0 40 36" width="40"><circle cx="15" cy="13" r="8" fill="none" stroke="#fff" stroke-width="4" stroke-dasharray="3 2"/><circle cx="15" cy="13" r="3" fill="#fff"/><circle cx="28" cy="27" r="6" fill="none" stroke="#fff" stroke-width="3.5" stroke-dasharray="3 2"/><circle cx="28" cy="27" r="2" fill="#fff"/></svg>
    <h3>Engineering</h3>
    <p>Lorem Ipsum is simply dummy text of the printing and typesetting industry. Lorem Ipsum has been the industry's</p>
  </div>
  <div class="abs service" style="left:353px">
    <svg viewBox="0 0 40 36" width="40"><path d="M4 22 12 4l4 2-5 12z" fill="#222"/><path d="M4 22h6v6H3z" fill="#222"/><rect x="16" y="16" width="16" height="10" fill="#222"/><rect x="14" y="27" width="24" height="6" rx="3" fill="#222"/></svg>
    <h3>Construction</h3>
    <p>Lorem Ipsum is simply dummy text of the printing and typesetting industry. Lorem Ipsum has been the industry's</p>
  </div>
  <div class="abs service" style="left:496px">
    <svg viewBox="0 0 40 36" width="40"><circle cx="20" cy="5" r="3" fill="none" stroke="#222" stroke-width="2"/><path d="M19 8 9 34M21 8l10 26M8 22q12 6 24 0" stroke="#222" stroke-width="2.5" fill="none"/></svg>
    <h3>Operations</h3>
    <p>Lorem Ipsum is simply dummy text of the printing and typesetting industry. Lorem Ipsum has been the industry's</p>
  </div>
  <div class="abs divider" style="top:728px"></div>
</section>

<section>
  <h2 class="abs head" style="left:78px;top:755px;font-weight:400">Articles</h2>
  <div class="abs acc-open">
    <span class="tab"></span><span class="bar"></span>
    <h4>Lorem ipsum dolor sit amet, consectetur adipisicing elit</h4>
    <p>Lorem Ipsum is simply dummy text of the printing and typesetting industry. Lorem Ipsum has been the industry's standard dummy text ever since the 1500s, when an unknown printer took a galley of type and scrambled it to make a type specimen book. It has survived not only five centuries, but also the leap into electronic typesetting, remaining essentially unchanged. It was popularised in the 1960s.</p>
  </div>
  <div class="abs acc" style="top:914px;height:23px"><i></i>Lorem ipsum dolor sit amet, consectetur adipisicing elit</div>
  <div class="abs acc" style="top:943px;height:23px"><i></i>Lorem ipsum dolor sit amet,</div>
  <div class="abs acc" style="top:972px;height:32px"><i></i>Lorem ipsum dolor sit amet, consectetur adipisicing elit</div>

  <h2 class="abs head" style="left:377px;top:755px;font-weight:400">News</h2>
  <div class="abs news" style="top:782px"><div class="date"><div class="d">27</div><div class="m">Feb</div></div><h5>Lorem ipsum dolor sit amet,</h5><p>Lorem Ipsum is simply dummy text of the printing and typesetting industry</p></div>
  <div class="abs news" style="top:841px"><div class="date"><div class="d">23</div><div class="m">Feb</div></div><h5>Lorem ipsum dolor sit amet,</h5><p>Lorem Ipsum is simply dummy text of the printing and typesetting industry.</p></div>
  <div class="abs news" style="top:900px"><div class="date"><div class="d">22</div><div class="m">Feb</div></div><h5>Lorem ipsum dolor sit amet,</h5><p>Lorem Ipsum is simply dummy text of the printing and typesetting industry. Lorem Ipsum has been the industry's standard dummy text</p></div>
  <div class="abs news" style="top:962px"><div class="date"><div class="d">23</div><div class="m">Feb</div></div><h5>Lorem ipsum dolor sit amet,</h5><p>Lorem Ipsum is simply dummy text of the printing and typesetting industry.</p></div>
</section>

<footer>
  <div class="abs foot">
    <div class="logo"><span></span><b>VANGRIDEX</b></div>
    <p class="about">Lorem Ipsum is simply dummy text of the printing and typesetting industry.</p>
    <span class="sep" style="left:207px"></span>
    <h6 style="left:238px;top:21px">Site Map</h6>
    <ul style="left:239px;top:44px"><li>Home</li><li>Business Units</li><li>Services</li><li>About Us</li><li>Locations</li><li>Contact Us</li></ul>
    <span class="sep" style="left:319px"></span>
    <h6 style="left:346px;top:21px">Get in touch</h6>
    <p class="contact">Toll-Free: 1-800-555-0176<br>Local: 555-010-4488<br>Fax: 555-010-4489</p>
    <h6 style="left:483px;top:21px">Map</h6>
    <div class="map" role="img" aria-label="Street map showing the office location"></div>
  </div>
  <div class="abs copy">Copyright © 2014 Vangridex . All rights reserved.</div>
</footer>

</body>
</html>
```